Dentist Seminar invite please see .doc in attachments

Need an 8.5 x 11 invite designed. It will be for an invitation to attend an evening seminar on dental procedures. Feel free to utilize both front and back ONLY IF REQUIRED

See Assets & PPT with additional assets.

INSPIRATION: FIle NAME BRELOW

Target Market(s)

Dentists

Industry/Entity Type

Dental

Font styles to use
Other font styles liked:
• lato, garamond, palatino linotype

Colors
cee9f5
9bcb3c
0492cd
cadf82

Requirements
Must have
• Must have the colours suggested, and professional feel.
• Some of the assets merged cleanly into the design
Should not have
• Any pictures of teeth, tooth brushes or any dental product

```html
<!DOCTYPE html>
<html lang="en">
<head>
<meta charset="utf-8">
<title>Dental Seminar Invitation</title>
<link rel="stylesheet" href="https://fonts.googleapis.com/css2?family=Lato:wght@300;400;700;900&display=swap">
<style>
  :root {
    --sky: #cee9f5;
    --lime: #9bcb3c;
    --blue: #0492cd;
    --pale-lime: #cadf82;
    --yellow: #f2ea2e;
    --charcoal: #4b4b4f;
    --ink: #3a3a3c;
    --muted: #6b6b6e;
    --paper: #ffffff;
    --stage: #ffffff;
  }
  * { box-sizing: border-box; margin: 0; padding: 0; }
  html, body {
    width: 1200px; height: 713px; overflow: hidden;
    background: var(--stage);
    font-family: "Lato", Arial, sans-serif;
    color: var(--ink);
  }
  .canvas { position: relative; width: 1200px; height: 713px; }
  .page {
    position: absolute; top: 40px;
    width: 408px; height: 527px;
    background: var(--paper);
    overflow: hidden;
    box-shadow: 0 0 0 1px #d8d8d8;
  }
  .page--back { left: 161px; }
  .page--front { left: 631px; }
  .page-art { position: absolute; inset: 0; width: 100%; height: 100%; }

  .body-copy { position: absolute; font-size: 6px; line-height: 8px; color: var(--ink); }
  .back-intro { left: 32px; top: 52px; width: 200px; }
  .back-topics { left: 32px; top: 404px; width: 160px; }
  .back-topics p + p { margin-top: 7px; }

  .bio-title { position: absolute; left: 30px; top: 26px; font-size: 13px; font-weight: 700; color: var(--ink); }
  .bio-copy { left: 27px; top: 52px; width: 250px; font-size: 5.6px; line-height: 7.4px; }

  .event-details {
    position: absolute; right: 14px; top: 336px;
    text-align: right; color: var(--paper);
    font-size: 12.5px; line-height: 16px; font-weight: 400;
  }
  .event-details .venue { margin-top: 16px; }

  .registration { position: absolute; left: 30px; top: 402px; }
  .registration-title { font-size: 15px; color: var(--muted); font-weight: 400; }
  .registration-email,
  .registration-phone { display: block; font-weight: 900; color: var(--muted); white-space: nowrap; }
  .registration-email { font-size: 24px; line-height: 28px; margin-top: 8px; letter-spacing: 0.1px; }
  .registration-phone { font-size: 32px; line-height: 34px; letter-spacing: 0.5px; }

  .swatch { position: absolute; top: 605px; width: 52px; height: 58px; }
  .swatch--lime { left: 161px; background: linear-gradient(90deg, var(--yellow), var(--lime)); }
  .swatch--blue { left: 239px; background: var(--blue); }
  .swatch--pale { left: 333px; background: linear-gradient(90deg, var(--pale-lime), var(--lime)); }
</style>
</head>
<body>
<main class="canvas">

  <section class="page page--back" aria-label="Invitation back">
    <svg class="page-art" viewBox="0 0 408 527" xmlns="http://www.w3.org/2000/svg">
      <defs>
        <linearGradient id="back-lime" x1="0" y1="0" x2="1" y2="0">
          <stop offset="0" stop-color="#d9ea9a"/>
          <stop offset="1" stop-color="#9bcb3c"/>
        </linearGradient>
        <linearGradient id="back-photo" x1="0" y1="0" x2="1" y2="1">
          <stop offset="0" stop-color="#5a1f24"/>
          <stop offset="0.45" stop-color="#b8484c"/>
          <stop offset="1" stop-color="#e9d9c4"/>
        </linearGradient>
        <linearGradient id="back-bridge" x1="0" y1="0" x2="0" y2="1">
          <stop offset="0" stop-color="#9fd08a"/>
          <stop offset="0.5" stop-color="#8a3c7c"/>
          <stop offset="1" stop-color="#e6e27a"/>
        </linearGradient>
      </defs>
      <polygon class="accent-lime" points="233,0 408,0 408,58 353,82" fill="url(#back-lime)"/>
      <polygon class="band-dark" points="168,368 408,253 408,527 300,527" fill="#4b4b4f"/>
      <polygon class="photo-area" points="168,175 408,60 408,253 168,368" fill="url(#back-photo)" role="img" aria-label="Clinical photograph of a dental implant being placed"/>
      <rect class="illustration-area" x="255" y="330" width="140" height="122" rx="18" fill="url(#back-bridge)" role="img" aria-label="3D illustration of an implant-supported bridge"/>
    </svg>

    <div class="body-copy back-intro">
      Recent advances in digital technology and its use in dentistry have introduced tools that can improve upon traditional methods. The use of modern 3D technology and the digital workflow procedures enhancing the predictability of the surgical plan, the state of the art diagnostic imaging technologies, digital fabrication, and 3D printing: multiple digital workflows will be discussed through real clinical cases. This groundbreaking lecture will showcase the synergy between fundamental biological principles to revolutionize surgery and implantology. Multiple innovative clinical cases will be presented with detail never seen before.
    </div>

    <div class="body-copy back-topics">
      <p>Digital technologies like 3D printing, new procedures and use of 3D planning in daily practice.</p>
      <p>Guided surgery and the use of surgical templates in the clinic.</p>
      <p>Digital technology in surgical treatment planning, guided navigation surgery and its applications, techniques like digitally guided bone block harvesting and osteotomy guides. Automated design software can improve upon real live surgery.</p>
    </div>
  </section>

  <section class="page page--front" aria-label="Invitation front">
    <svg class="page-art" viewBox="0 0 408 527" xmlns="http://www.w3.org/2000/svg">
      <defs>
        <linearGradient id="front-paper" x1="0" y1="0" x2="1" y2="0">
          <stop offset="0" stop-color="#d2d2d4"/>
          <stop offset="1" stop-color="#ffffff"/>
        </linearGradient>
        <linearGradient id="front-lime" x1="0" y1="0" x2="1" y2="0">
          <stop offset="0" stop-color="#d9ea9a"/>
          <stop offset="1" stop-color="#9bcb3c"/>
        </linearGradient>
        <linearGradient id="front-jaw" x1="0" y1="0" x2="1" y2="1">
          <stop offset="0" stop-color="#c9c9cb"/>
          <stop offset="0.5" stop-color="#a6a6a8"/>
          <stop offset="1" stop-color="#e2e2e3"/>
        </linearGradient>
        <linearGradient id="front-skull" x1="0" y1="0" x2="0" y2="1">
          <stop offset="0" stop-color="#f4efe0"/>
          <stop offset="1" stop-color="#d9d2bd"/>
        </linearGradient>
      </defs>
      <rect width="408" height="527" fill="url(#front-paper)"/>
      <polygon class="accent-lime" points="232,0 408,0 408,84 380,84" fill="url(#front-lime)"/>
      <polygon class="illustration-area" points="168,172 408,58 408,258 168,367" fill="url(#front-jaw)" role="img" aria-label="3D render of a lower jaw with colour-coded teeth and an implant"/>
      <polygon class="band-dark" points="168,367 408,258 408,527" fill="#4b4b4f"/>
      <polygon class="accent-blue" points="5,250 168,172 168,367" fill="#0492cd"/>
      <rect class="illustration-area" x="44" y="229" width="116" height="74" rx="14" fill="url(#front-skull)" role="img" aria-label="3D render of an upper jaw model"/>
    </svg>

    <h2 class="bio-title">Biography</h2>
    <p class="body-copy bio-copy">
      Our speaker is a clinician and educator with over fifteen years of experience in implant dentistry and digital surgical planning. They lecture internationally on guided surgery, 3D imaging and digital workflows, and maintain a private practice focused on complex restorative cases. Their research explores how automated design software and printed surgical guides can improve predictability, reduce chair time and support better outcomes for patients in everyday clinical practice across a wide range of treatment needs.
    </p>

    <div class="event-details">
      <p>November 13, 2017</p>
      <p>6:30 – 9:30pm</p>
      <p class="venue">Maple Hall Banquet Centre</p>
      <p>2048 Orchard St.</p>
      <p>Toronto, Ontario</p>
      <p>M1A 0B1</p>
    </div>

    <div class="registration">
      <h3 class="registration-title">Registration:</h3>
      <span class="registration-email">rsvp@smileforum.ca</span>
      <span class="registration-phone">416-555-0187</span>
    </div>
  </section>

  <div class="swatch swatch--lime" aria-hidden="true"></div>
  <div class="swatch swatch--blue" aria-hidden="true"></div>
  <div class="swatch swatch--pale" aria-hidden="true"></div>

</main>
</body>
</html>
```